Insurance Agency website design for Halvern Crest Insurance, LP

Build a website for Halvern Crest Insurance, LP which sells Homeowners, Auto, Renters, Condo, Flood, Disability, Life, Umbrella, and health insurance. We need the coolest insurance agency website out there to get quotes, contact us, or get additional information. Please list the following insurance companies we work with: Dravo, Velk, Meridale Union, Tarvix, Brookwynd, QZT, and Pellurian.

Target Market(s)

Make a design similar to https://www.fandelmora.example/

Industry/Entity Type

Selling personal insurance policies

Coding

Coded - Design and coding required

Number of Pages Required

3 page

```html
<!DOCTYPE html>
<html lang="en">
<head>
<meta charset="utf-8">
<title>Halvern Crest Insurance, LP</title>
<link href="https://fonts.googleapis.com/css2?family=Lexend:wght@500;600;700&family=Inter:wght@400;500;600;700&display=swap" rel="stylesheet">
<style>
:root{
  --navy:#0b4a8b;
  --navy-deep:#0a3f78;
  --ink:#0d2f5c;
  --orange:#ff6a00;
  --sky:#e8f2fc;
  --text:#3d4552;
  --white:#fff;
}
*{box-sizing:border-box;margin:0;padding:0}
html,body{width:1200px;height:5059px;overflow:hidden}
body{font-family:"Inter",sans-serif;color:var(--text);background:var(--white);position:relative}
h1,h2,h3,h4{font-family:"Lexend",sans-serif;color:var(--ink)}
.abs{position:absolute}
.btn{display:inline-flex;align-items:center;gap:8px;background:var(--orange);color:#fff;font-weight:600;font-size:14px;padding:0 26px;height:42px;border-radius:22px;text-decoration:none;box-shadow:0 3px 0 rgba(0,0,0,.12)}
.btn svg{width:14px;height:14px}
.label{font-size:13px;font-weight:600;color:var(--navy)}
.label em{font-style:normal;color:var(--orange)}
.center{text-align:center}

/* top bar */
.topbar{top:0;left:0;width:1200px;height:40px;background:var(--navy);color:#fff;font-size:12px}
.topbar .social{left:60px;top:12px;display:flex;gap:30px}
.dot{width:12px;height:12px;border-radius:50%;background:#fff;opacity:.9}
.topbar .links{right:62px;top:12px;display:flex;gap:18px}
/* nav */
.nav{top:40px;left:0;width:1200px;height:78px;background:#fff}
.brand{display:flex;align-items:center;gap:10px;font-family:"Lexend",sans-serif;font-weight:700;color:var(--navy);font-size:18px}
.brand i{width:30px;height:30px;border-radius:50%;background:var(--orange);display:block}
.nav .brand{left:62px;top:24px}
.menu{left:380px;top:32px;display:flex;gap:36px;font-size:14px;font-weight:500;color:var(--ink)}
.menu .on{color:var(--navy);font-weight:600}
.agent{left:790px;top:20px;display:flex;gap:10px;align-items:center}
.agent .ring{width:38px;height:38px;border-radius:50%;border:2px solid var(--navy);display:flex;align-items:center;justify-content:center}
.agent small{display:block;font-size:11px;color:var(--text)}
.agent b{font-size:14px;color:var(--navy)}
.nav .btn{left:993px;top:20px;height:38px;font-size:14px}
/* hero */
.hero{top:118px;left:0;width:1200px;height:514px;overflow:hidden}
.hero-bg{position:absolute;inset:0;background:linear-gradient(100deg,#f4efe9 0%,#e9e1d6 38%,#c9b8a3 62%,#6f8fb3 100%)}
.hero h1{left:62px;top:130px;font-size:48px;line-height:54px;color:var(--ink);font-weight:700}
.hero p{left:62px;top:256px;width:440px;font-size:17px;line-height:27px;color:#2b3441}
.hero .btn{left:62px;top:334px}
/* panels */
.panel{top:632px;width:600px;height:266px}
.panel.blue{left:0;background:var(--navy-deep)}
.panel.orange{left:600px;background:var(--orange)}
.frame{width:150px;height:150px;border-radius:40px 40px 40px 12px;border:2px dashed rgba(255,255,255,.8);padding:8px}
.frame div{width:100%;height:100%;border-radius:34px 34px 34px 8px}
.panel h3{color:#fff;font-size:27px;font-weight:700}
.panel p{color:#fff;font-size:14px;font-weight:600;line-height:24px}
.btn.white{background:#fff;color:var(--orange);height:38px}
.btn.dark{background:var(--navy-deep);color:#fff;height:38px}
/* about */
.about-img{left:64px;top:986px;width:472px;height:366px;border-radius:12px;background:linear-gradient(135deg,#c8b49c,#7f6b5a 55%,#3c5a74)}
.about .label{left:600px;top:982px}
.about h2{left:600px;top:1008px;font-size:34px;font-weight:700}
.about p{left:600px;width:530px;font-size:14px;line-height:24px}
/* stats */
.stats{top:1438px;left:0;width:1200px;height:172px;background:var(--navy)}
.stat{top:56px;display:flex;gap:14px;align-items:center;color:#fff}
.stat b{font-family:"Lexend",sans-serif;font-size:35px;font-weight:600;display:block;line-height:38px}
.stat span{font-size:13px}
/* cards */
.card{background:var(--sky);border-radius:8px;overflow:hidden}
.card .ph{height:237px}
.iconbub{position:absolute;width:98px;height:98px;border-radius:0 0 48px 48px;background:#fff;border:2px solid #fff;box-shadow:0 4px 10px rgba(0,0,0,.1);display:flex;align-items:center;justify-content:center}
.card h4{font-size:18px;font-weight:600;line-height:24px;text-align:center;color:#111}
/* agents */
.agents{top:2392px;left:0;width:1200px;height:558px;background:var(--navy)}
.agents h2{color:#fff;font-size:36px;line-height:41px}
.agents p{color:#fff;font-size:14px;line-height:24px;font-weight:500}
/* testimonials */
.tcard{top:3148px;width:342px;height:296px;background:#fff;border-radius:8px;box-shadow:0 4px 22px rgba(12,50,100,.09);padding:28px 24px}
.tcard .head{display:flex;gap:12px;align-items:center}
.tcard .g{width:34px;height:34px;border-radius:50%;background:var(--sky)}
.stars{color:var(--orange);font-size:14px;letter-spacing:2px}
.tcard .head small{display:block;font-size:14px;color:#333}
.tcard p{margin-top:22px;font-size:14px;line-height:24px;color:#555;border-bottom:1px solid #ddd;padding-bottom:14px}
.tcard h5{margin-top:14px;font-size:14px;color:#222}
.tcard .role{font-size:12px;color:#666}
/* partners */
.partners{top:3575px;left:0;width:1200px;height:173px;background:var(--sky);display:flex;align-items:center;justify-content:space-between;padding:0 64px}
.partners span{font-family:"Inter",sans-serif;font-weight:700;font-size:22px;color:#1b2a3d;letter-spacing:1px}
/* tips */
.tip{width:396px;height:440px}
.tip h4{font-size:18px;line-height:25px;text-align:center;color:#111;margin-top:26px}
.tip p{font-size:14px;line-height:24px;text-align:center;color:#555;margin:10px 22px 0}
.tip .more{display:block;text-align:center;color:var(--orange);font-weight:600;font-size:14px;margin-top:16px}
/* footer */
.footer{top:4590px;left:0;width:1200px;height:469px;background:var(--navy-deep);color:#fff}
.footer h4{color:#fff;font-size:18px;font-weight:600}
.footer ul{list-style:none;font-size:14px;line-height:33px}
.footer .copy{left:0;top:422px;width:1200px;text-align:center;font-size:14px;border-top:1px solid rgba(255,255,255,.15);padding-top:20px;top:405px}
.sring{width:42px;height:42px;border-radius:50%;border:1.5px solid rgba(255,255,255,.7)}
</style>
</head>
<body>

<!-- top bar -->
<div class="abs topbar">
  <div class="abs social"><span class="dot"></span><span class="dot"></span><span class="dot"></span><span class="dot"></span></div>
  <div class="abs links"><span>Are you an agent?</span><span>Sign up</span><span>|</span><span>Log in</span></div>
</div>

<!-- nav -->
<header class="abs nav">
  <div class="abs brand"><i></i>Halvern Crest Insurance</div>
  <nav class="abs menu"><span class="on">Home</span><span>About Us</span><span>Insurance ⌄</span><span>Contact Us</span></nav>
  <div class="abs agent">
    <div class="ring"><svg width="18" height="18" viewBox="0 0 24 24" fill="none" stroke="#0b4a8b" stroke-width="2"><path d="M5 3h4l2 5-3 2a11 11 0 006 6l2-3 5 2v4a2 2 0 01-2 2A17 17 0 013 5a2 2 0 012-2z"/></svg></div>
    <div><small>Talk to an agent</small><b>(612) 555-0148</b></div>
  </div>
  <a class="abs btn">Get A Quote</a>
</header>

<!-- hero -->
<section class="abs hero">
  <div class="hero-bg" role="img" aria-label="Hands sheltering wooden family figures beside checklist of home, car and health icons"></div>
  <h1 class="abs">Choosing The Best<br>Insurance For You</h1>
  <p class="abs">At Halvern Crest Insurance, we understand that your peace of mind is invaluable.</p>
  <a class="abs btn">Get Started <svg viewBox="0 0 16 16" fill="none" stroke="#fff" stroke-width="2"><path d="M2 8h11M9 4l4 4-4 4"/></svg></a>
</section>

<!-- panels -->
<section class="abs panel blue">
  <div class="abs frame" style="left:64px;top:56px"><div role="img" aria-label="Smiling agent portrait" style="background:linear-gradient(160deg,#ff8a33,#e45c00)"></div></div>
  <h3 class="abs" style="left:236px;top:56px;font-size:25px">Halvern Crest Insurance</h3>
  <p class="abs" style="left:236px;top:100px;width:330px;text-align:center">Homeowners | Auto | Renters |<br>Condo | Food and much more</p>
  <a class="abs btn white" style="left:282px;top:164px">Find Out More Insurance →</a>
</section>
<section class="abs panel orange">
  <h3 class="abs" style="left:32px;top:56px">For Any Kind Inquiries</h3>
  <p class="abs" style="left:32px;top:100px;width:310px;text-align:center">Please contact us at :(612) 555-0148<br>or <u>info@halverncrest.example</u></p>
  <a class="abs btn dark" style="left:60px;top:164px">For More Info Contact Us →</a>
  <div class="abs frame" style="left:382px;top:56px"><div role="img" aria-label="Smiling advisor giving thumbs up" style="background:linear-gradient(160deg,#1d5fa6,#0a3f78)"></div></div>
</section>

<!-- about -->
<section class="about">
  <div class="abs about-img" role="img" aria-label="Advisor meeting a young couple at a desk"></div>
  <div class="abs label">About Us</div>
  <h2 class="abs">About Halvern Crest Insurance</h2>
  <p class="abs" style="top:1068px">Halvern Crest Insurance is a full-service, independent insurance agency with over three decades of experience in delivering comprehensive insurance solutions to individuals.</p>
  <p class="abs" style="top:1164px">We proudly offer a diverse portfolio of products from more than 20 of the most reputable and financially secure companies in the industry. Our dedicated team of over 50 skilled professionals is committed to customizing these products and services to meet the unique needs of each client.</p>
  <a class="abs btn" style="left:600px;top:1310px">Read More →</a>
</section>

<!-- stats -->
<section class="abs stats">
  <div class="abs stat" style="left:62px"><svg width="48" height="48" viewBox="0 0 48 48"><path d="M4 24a20 20 0 0140 0z" fill="#ff6a00"/><path d="M24 24v14a4 4 0 01-8 0" stroke="#fff" stroke-width="3" fill="none"/></svg><div><b>300+</b><span>Give Insurances</span></div></div>
  <div class="abs stat" style="left:330px"><svg width="48" height="48" viewBox="0 0 48 48"><circle cx="20" cy="14" r="9" fill="#fff"/><path d="M4 42a16 16 0 0132 0z" fill="#fff"/><circle cx="36" cy="32" r="9" fill="#ff6a00"/><path d="M36 27v10M31 32h10" stroke="#fff" stroke-width="2.5"/></svg><div><b>50+</b><span>Skilled Professionals</span></div></div>
  <div class="abs stat" style="left:634px"><svg width="48" height="48" viewBox="0 0 48 48"><circle cx="24" cy="24" r="20" fill="#fff"/><circle cx="24" cy="24" r="9" fill="#0b4a8b"/><path d="M24 4a20 20 0 0120 20H33a9 9 0 00-9-9zM24 44A20 20 0 014 24h11a9 9 0 009 9z" fill="#ff6a00"/></svg><div><b>130+</b><span>Ongoing Insurance</span></div></div>
  <div class="abs stat" style="left:918px"><svg width="52" height="48" viewBox="0 0 52 48"><path d="M26 26l-10-10a6 6 0 0110-7 6 6 0 0110 7z" fill="#ff6a00"/><path d="M2 36h12l10 4h14l12-8M14 36l8-4h10" stroke="#fff" stroke-width="3" fill="none"/></svg><div><b>250+</b><span>Satisfied Customers</span></div></div>
</section>

<!-- focus -->
<section>
  <div class="abs label center" style="left:0;top:1696px;width:1200px">Focusing On Your <em>Needs</em></div>
  <h2 class="abs center" style="left:0;top:1720px;width:1200px;font-size:34px;line-height:40px">Our Experts Are Focused on<br>Addressing The Individual Needs</h2>
  <div class="abs card" style="left:192px;top:1850px;width:396px;height:456px">
    <div class="ph" role="img" aria-label="Couple holding a small model house" style="background:linear-gradient(135deg,#d9cdbf,#8a7a6c)"></div>
  </div>
  <div class="abs iconbub" style="left:341px;top:2040px"><svg width="44" height="44" viewBox="0 0 44 44"><path d="M10 22l12-10 12 10v12H10z" fill="#ff6a00"/><path d="M4 18a18 18 0 0136 0M40 28a18 18 0 01-36 0" stroke="#0b4a8b" stroke-width="3" fill="none"/></svg></div>
  <h4 class="abs" style="left:192px;top:2164px;width:396px;font-size:18px;text-align:center;color:#111;line-height:24px">We are Dedicated To<br>Safeguarding Your Assets</h4>
  <a class="abs btn" style="left:300px;top:2230px;height:38px">Find Out More →</a>

  <div class="abs card" style="left:612px;top:1850px;width:396px;height:456px">
    <div class="ph" role="img" aria-label="Family of three smiling on a sofa" style="background:linear-gradient(135deg,#c3ccd6,#6d7f94)"></div>
  </div>
  <div class="abs iconbub" style="left:761px;top:2040px"><svg width="44" height="44" viewBox="0 0 44 44"><path d="M6 20a16 16 0 0132 0z" fill="#ff6a00"/><circle cx="15" cy="26" r="3" fill="#0b4a8b"/><circle cx="29" cy="26" r="3" fill="#0b4a8b"/><circle cx="22" cy="29" r="2.5" fill="#0b4a8b"/><path d="M11 40v-8h8v8M25 40v-8h8v8M19 40v-6h6v6" fill="#0b4a8b"/></svg></div>
  <h4 class="abs" style="left:612px;top:2164px;width:396px;font-size:18px;text-align:center;color:#111;line-height:24px">Providing You With<br>The Security You Deserve.</h4>
  <a class="abs btn" style="left:722px;top:2230px;height:38px">Contact Us →</a>
</section>

<!-- agents -->
<section class="abs agents">
  <div class="abs" style="left:62px;top:126px;color:#fff;font-size:13px;font-weight:600">Find Your Best Agents</div>
  <h2 class="abs" style="left:62px;top:152px">Find Our Best Agents<br>Near About You</h2>
  <p class="abs" style="left:62px;top:246px;width:430px">Lorem ipsum dolor sit ameto consectetur adipisicing elitos sed do eiusmod tempor incididunt ut labore etos dolore se magna aliq Ut enim ad minim veniam quis nos trud exercit ation ullamco laboris nisi ut aliquip ex ea commodo consequat uis aute irure dolor</p>
  <a class="abs btn" style="left:62px;top:390px">Find Your Agent →</a>
  <svg class="abs" style="left:520px;top:80px" width="620" height="420" viewBox="0 0 620 420" fill="none">
    <path d="M250 120C270 60 320 10 400 8H612V330C612 380 560 408 500 408H250C240 380 230 330 230 300" stroke="#fff" stroke-width="2" stroke-dasharray="8 6"/>
    <path d="M8 140H190C230 140 250 180 250 220V408H40C20 408 8 390 8 370z" stroke="#fff" stroke-width="2" stroke-dasharray="8 6"/>
  </svg>
  <div class="abs" role="img" aria-label="Smiling agent talking on the phone in an office" style="left:786px;top:108px;width:330px;height:330px;border-radius:110px 0 0 0;background:linear-gradient(150deg,#e9edf2,#9aa7b6 60%,#2c3e56)"></div>
  <div class="abs" role="img" aria-label="Cheerful customer on a phone call" style="left:540px;top:250px;width:200px;height:200px;border-radius:0 0 0 0;border-top-right-radius:70px;background:linear-gradient(150deg,#d7c3b0,#8b6f58)"></div>
  <div class="abs" style="left:690px;top:208px;background:#fff;border-radius:22px;padding:12px 28px;font-family:'Lexend',sans-serif;font-weight:600;font-size:17px;color:var(--orange)">Perfect Match</div>
</section>

<!-- testimonials -->
<section>
  <div class="abs label center" style="left:0;top:3034px;width:1200px">Client <em>Testimonial</em></div>
  <h2 class="abs center" style="left:0;top:3060px;width:1200px;font-size:34px">What Our Clients Say About Us</h2>
  <div class="abs tcard" style="left:64px"><div class="head"><span class="g"></span><div><span class="stars">★★★★★</span><small><b>4.5</b> out of 5.0</small></div></div><p>Lorem ipsum dolor sit amet consecte tur adipisicing elit sed do eiusmod temporoi incididunt ut labore et dolore magna aliq Ut enim ad minim veniam nostrud exerct tation ullamco laboris nisi dolore.</p><h5>Lena Corvath</h5><div class="role">Customer</div></div>
  <div class="abs tcard" style="left:429px"><div class="head"><span class="g"></span><div><span class="stars">★★★★★</span><small><b>4.5</b> out of 5.0</small></div></div><p>Lorem ipsum dolor sit amet consecte tur adipisicing elit sed do eiusmod temporoi incididunt ut labore et dolore magna aliq Ut enim ad minim veniam nostrud exerct tation ullamco laboris nisi dolore.</p><h5>Lena Corvath</h5><div class="role">Customer</div></div>
  <div class="abs tcard" style="left:794px"><div class="head"><span class="g"></span><div><span class="stars">★★★★★</span><small><b>4.5</b> out of 5.0</small></div></div><p>Lorem ipsum dolor sit amet consecte tur adipisicing elit sed do eiusmod temporoi incididunt ut labore et dolore magna aliq Ut enim ad minim veniam nostrud exerct tation ullamco laboris nisi dolore.</p><h5>Lena Corvath</h5><div class="role">Customer</div></div>
  <svg class="abs" style="left:562px;top:3480px" width="80" height="20"><circle cx="12" cy="10" r="8" fill="none" stroke="#ff6a00" stroke-width="1.5"/><circle cx="12" cy="10" r="3" fill="#ff6a00"/><circle cx="41" cy="10" r="3" fill="#777"/><circle cx="70" cy="10" r="3" fill="#777"/></svg>
</section>

<!-- partners -->
<section class="abs partners">
  <span>Dravo</span><span>Velk</span><span>Brookwynd</span><span>Meridale Union</span><span>Tarvix</span><span>Pellurian</span>
</section>

<!-- tips -->
<section>
  <div class="abs label center" style="left:0;top:3836px;width:1200px">Latest Insurance <em>Tips</em></div>
  <h2 class="abs center" style="left:0;top:3862px;width:1200px;font-size:34px;line-height:40px">Sed Ut Perspiciatis Unde Omnis<br>Sit Voluptatem Accusantium Dolorem</h2>
  <div class="abs card tip" style="left:192px;top:3988px">
    <div class="ph" style="height:218px;background:linear-gradient(135deg,#eae6e1,#9c8c7d)" role="img" aria-label="Couple shaking hands with an agent"></div>
    <h4>Ut Enim Ad Minima Veni<br>Puisam Nostrum Exercitatos</h4>
    <p>Lorem ipsum dolor sit amet consecte tur adipisi cing elit sed do eiusmod temporoi incididunto ut labore et dolores sid</p>
    <span class="more">Read More →</span>
  </div>
  <div class="abs card tip" style="left:612px;top:3988px">
    <div class="ph" style="height:218px;background:linear-gradient(135deg,#f1e8dc,#c3a584)" role="img" aria-label="Wooden house, car and family figures on a block"></div>
    <h4>Ut Enim Ad Minima Veni<br>Puisam Nostrum Exercitatos</h4>
    <p>Lorem ipsum dolor sit amet consecte tur adipisi cing elit sed do eiusmod temporoi incididunto ut labore et dolores sid</p>
    <span class="more">Read More →</span>
  </div>
  <a class="abs btn" style="left:502px;top:4464px;height:40px">View More News →</a>
</section>

<!-- footer -->
<footer class="abs footer">
  <div class="abs brand" style="left:62px;top:104px;color:#fff"><i></i>Halvern Crest Insurance</div>
  <p class="abs" style="left:62px;top:152px;width:290px;font-size:14px;line-height:24px">At Halvern Crest Insurance, we understand that your peace of mind is invaluable. Our mission is to protect what matters most to you.</p>
  <div class="abs" style="left:62px;top:262px;display:flex;gap:10px"><span class="sring"></span><span class="sring"></span><span class="sring"></span><span class="sring"></span></div>
  <h4 class="abs" style="left:416px;top:100px">Quick Links</h4>
  <ul class="abs" style="left:416px;top:138px"><li>Home</li><li>About Us</li><li>Insurance</li><li>Latest Blog</li><li>Contact Us</li></ul>
  <h4 class="abs" style="left:604px;top:100px">Our Insurance</h4>
  <ul class="abs" style="left:604px;top:138px"><li>Homeowners</li><li>Auto</li><li>Renters</li><li>Condo</li><li>Flood</li></ul>
  <ul class="abs" style="left:724px;top:138px"><li>Disability</li><li>Life</li><li>Umbrella</li><li>Health</li></ul>
  <h4 class="abs" style="left:870px;top:100px">Contact Information</h4>
  <div class="abs" style="left:870px;top:142px;display:flex;gap:14px;font-size:14px;line-height:22px"><svg width="18" height="22" viewBox="0 0 18 22"><path d="M9 1a7 7 0 00-7 7c0 5 7 13 7 13s7-8 7-13a7 7 0 00-7-7z" fill="none" stroke="#ff6a00" stroke-width="2"/><circle cx="9" cy="8" r="2.5" fill="#ff6a00"/></svg><span>48 Alder Row, Brightwater,<br>California, USA</span></div>
  <div class="abs" style="left:870px;top:216px;display:flex;gap:14px;font-size:14px"><svg width="18" height="18" viewBox="0 0 24 24" fill="none" stroke="#ff6a00" stroke-width="2"><path d="M5 3h4l2 5-3 2a11 11 0 006 6l2-3 5 2v4a2 2 0 01-2 2A17 17 0 013 5a2 2 0 012-2z"/></svg><span>(612) 555-0148</span></div>
  <div class="abs" style="left:870px;top:268px;display:flex;gap:14px;font-size:14px"><svg width="18" height="16" viewBox="0 0 18 14" fill="none" stroke="#ff6a00" stroke-width="2"><rect x="1" y="1" width="16" height="12" rx="1"/><path d="M1 2l8 6 8-6"/></svg><span>info@halverncrest.example</span></div>
  <div class="abs copy">© 2025 Halvern Crest Insurance. All rights reserved.</div>
</footer>

</body>
</html>
```